Stationary Project for Single Designer: Vantor Graphic Design Agency

Stationary Project for single Designer: Vantor Graphic Design Agency (http://artists.plumbrook-studio.example/artist/52417)
As per previous discussion.
Business Stationary ($160)
Business card Wellbirch
Business Card Tendfield Post
In addition to the current deign you provided can we see one where you have the logo and the name along side the logo ie like the logo in design 4187396
Letter head Wellbirch
Letter Head Tendfield Post
Power point template Wellbirch
Address is: 7, Jalan Merbok 3B, Taman Merbok, 43300 Seri Kembangan, Selangor
For the business card will need phone number space for Malaysia and Australia
Development of Style Manual ($100)
Let me know if you want more detail
Updates
Sorry this was meant to be a job for a specific designer. Not sure how this went out to a competition format.

```html
<!DOCTYPE html>
<html lang="en">
<head>
<meta charset="utf-8">
<title>Tendfield Post Letterhead</title>
<link rel="stylesheet" href="https://fonts.googleapis.com/css2?family=Montserrat:wght@400;500;700&display=swap">
<style>
  :root {
    --brand-purple: #4a2a8c;
    --brand-orange: #f7a823;
    --text-grey: #5b5670;
    --soft-lavender: #e9e3f2;
    --soft-peach: #fdebd2;
    --paper: #ffffff;
  }
  html, body {
    margin: 0;
    padding: 0;
    overflow: hidden;
    background: var(--paper);
  }
  .letterhead {
    position: relative;
    width: 849px;
    height: 1200px;
    background: var(--paper);
    overflow: hidden;
    font-family: "Montserrat", sans-serif;
  }
  .brand {
    position: absolute;
    left: 46px;
    top: 58px;
    display: flex;
    align-items: center;
    gap: 14px;
  }
  .brand-dot {
    width: 34px;
    height: 34px;
    border-radius: 50%;
    background: var(--brand-orange);
  }
  .brand-name {
    font-size: 38px;
    font-weight: 700;
    color: var(--brand-purple);
    letter-spacing: -0.5px;
  }
  .brand-decoration {
    position: absolute;
    left: 480px;
    top: 660px;
    width: 369px;
    height: 540px;
    background: linear-gradient(160deg, var(--soft-lavender) 0%, var(--soft-lavender) 55%, var(--soft-peach) 100%);
    opacity: 0.8;
  }
  .contact {
    position: absolute;
    left: 28px;
    top: 878px;
    font-size: 11px;
    line-height: 14px;
    color: var(--text-grey);
  }
  .contact-row {
    display: flex;
  }
  .contact-label {
    width: 22px;
    flex: none;
  }
  .contact-group {
    margin-bottom: 12px;
  }
  .contact-web {
    margin-top: 16px;
    font-weight: 700;
    color: var(--brand-purple);
    font-size: 12px;
  }
</style>
</head>
<body>
  <div class="letterhead">
    <header class="brand">
      <span class="brand-dot"></span>
      <span class="brand-name">Tendfield Post</span>
    </header>

    <div class="brand-decoration" role="img" aria-label="Large faint brand symbol decoration in lavender and peach"></div>

    <footer class="contact">
      <div class="contact-group">
        <div class="contact-row"><span class="contact-label">A :</span><span>7, Jalan Merbok 3B<br>Taman Merbok<br>43300 Seri Kembangan<br>Selangor, Malaysia</span></div>
      </div>
      <div class="contact-group">
        <div class="contact-row"><span class="contact-label">T :</span><span>+00 0000 0000 (MY)</span></div>
        <div class="contact-row"><span class="contact-label">T :</span><span>+000 0000 0000 (AU)</span></div>
        <div class="contact-row"><span class="contact-label">E :</span><span>info@tendfieldpost.example</span></div>
      </div>
      <div class="contact-web">www.tendfieldpost.example</div>
    </footer>
  </div>
</body>
</html>
```